Managed Service Provider need new business cards

We are a small Maanged Service Provider of IT Services and need a new fresh design for our business cards. We want something impossible, fun and professional :)
Our services has a large range, but we are always fun and make sure our customers both get their issue sorted and also feel like they are "catching up with an old friend".
All our cards in the past has always been all black, with red and we need something fresher.
The back of card, we would like just a small list of what we do i think, but if someone has a better idea, please do something cool with the back of the card:
Managed IT Services
Productivity Solutions
Data Backup and Recovery
IT System Maintenance
Managed IT Security
More details can be found on our website qvtechworks.com.au
Industry/Entity Type
It Company
Contact Information for Business Card
Name: Simon Trelawny
Title: Director
Phone: 03 6158 4932
Mobile: 0417 582 139
Email: simon@qvtechworks.com.au
Web: www.qvtechworks.com.au
Look and feel
Each slider illustrates characteristics of the customer's brand and the style your logo design should communicate.

```html
<!DOCTYPE html>
<html lang="en">
<head>
<meta charset="utf-8">
<title>QV Techworks – Business Cards</title>
<link href="https://fonts.googleapis.com/css2?family=Anton&family=Roboto+Condensed:wght@500;700&family=Montserrat:wght@400;500&display=swap" rel="stylesheet">
<style>
  :root {
    --bg: #8a8a8a;
    --card: #050505;
    --red: #e3171f;
    --white: #ffffff;
  }
  * { margin: 0; padding: 0; box-sizing: border-box; }
  html, body { width: 1200px; height: 965px; overflow: hidden; }
  body {
    background: var(--bg);
    position: relative;
    font-family: "Montserrat", sans-serif;
  }
  .card {
    position: absolute;
    left: 260px;
    width: 680px;
    height: 415px;
    background: var(--card);
    box-shadow: 0 8px 24px rgba(0,0,0,.35);
    overflow: hidden;
  }
  .card--services { top: 30px; }
  .card--contact { top: 510px; }

  .brand {
    position: absolute;
    display: flex;
    align-items: center;
    gap: 14px;
    color: var(--red);
    font-family: "Anton", sans-serif;
    text-transform: uppercase;
    letter-spacing: 1px;
    line-height: 1;
    white-space: nowrap;
  }
  .brand__dot {
    width: 22px; height: 22px;
    border-radius: 50%;
    background: var(--red);
  }
  .card--services .brand { left: 60px; bottom: 80px; font-size: 58px; }
  .card--contact .brand { left: 50px; top: 200px; font-size: 42px; }

  .services {
    position: absolute;
    right: 90px;
    top: 70px;
    list-style: none;
    text-align: right;
    font-family: "Roboto Condensed", sans-serif;
    font-weight: 500;
    font-size: 22px;
    line-height: 1.3;
    color: var(--white);
    text-transform: uppercase;
  }
  .edge-dashes {
    position: absolute;
    right: 0; top: 70px;
    display: flex; flex-direction: column; gap: 14px;
  }
  .edge-dashes span {
    display: block; width: 14px; height: 12px; background: var(--red);
  }

  .person { position: absolute; left: 390px; top: 70px; }
  .person__name {
    font-family: "Roboto Condensed", sans-serif;
    font-weight: 700;
    font-size: 30px;
    color: var(--red);
    text-transform: uppercase;
    letter-spacing: .5px;
    white-space: nowrap;
  }
  .person__title { font-size: 18px; color: var(--white); margin-top: 2px; }

  .contact-list {
    position: absolute;
    list-style: none;
    color: var(--white);
    font-size: 18px;
  }
  .contact-list li { display: flex; align-items: center; gap: 10px; line-height: 1.5; white-space: nowrap; }
  .contact-list svg { width: 18px; height: 18px; flex: none; }
  .contact-list--phones { left: 410px; top: 180px; }
  .contact-list--web { right: 36px; top: 300px; }
  .accent { color: var(--red); }
  .foot-dash {
    position: absolute; left: 372px; bottom: 38px;
    width: 22px; height: 3px; background: var(--red);
  }
</style>
</head>
<body>

<section class="card card--services">
  <ul class="services">
    <li>Managed IT Services</li>
    <li>Productivity Solutions</li>
    <li>Data Backup and Recovery</li>
    <li>IT System Maintenance</li>
    <li>Managed IT Security</li>
  </ul>
  <div class="edge-dashes"><span></span><span></span><span></span><span></span><span></span></div>
  <div class="brand"><span class="brand__dot"></span>QV Techworks</div>
</section>

<section class="card card--contact">
  <div class="brand"><span class="brand__dot"></span>QV Techworks</div>

  <div class="person">
    <div class="person__name">Simon Trelawny</div>
    <div class="person__title">Director</div>
  </div>

  <ul class="contact-list contact-list--phones">
    <li>
      <svg viewBox="0 0 24 24" fill="none" stroke="#e3171f" stroke-width="2"><path d="M5 3h4l2 5-3 2a12 12 0 0 0 6 6l2-3 5 2v4a2 2 0 0 1-2 2A18 18 0 0 1 3 5a2 2 0 0 1 2-2z"/></svg>
      03 6158 4932
    </li>
    <li>
      <svg viewBox="0 0 24 24" fill="none" stroke="#e3171f" stroke-width="2"><rect x="6" y="2" width="12" height="20" rx="2"/><line x1="11" y1="18" x2="13" y2="18"/></svg>
      0417 582 139
    </li>
  </ul>

  <ul class="contact-list contact-list--web">
    <li>
      <svg viewBox="0 0 24 24" fill="none" stroke="#e3171f" stroke-width="2"><rect x="3" y="5" width="18" height="14"/><path d="M3 5l9 7 9-7"/></svg>
      simon@qvtechworks.com.au
    </li>
    <li>
      <svg viewBox="0 0 24 24" fill="none" stroke="#e3171f" stroke-width="2"><circle cx="12" cy="12" r="9"/><path d="M3 12h18M12 3c3 3 3 15 0 18M12 3c-3 3-3 15 0 18"/></svg>
      <span>www.<span class="accent">qvtechworks</span>.com.au</span>
    </li>
  </ul>
  <div class="foot-dash"></div>
</section>

</body>
</html>
```